Business Card Design Project

We need a business card design for an existing company in Dallas/Fort Worth that is expanding services and re-branding. We are changing the name from Brightmoor Commercial Cleaning to Keystride Facility Services. We are expanding from only commercial cleaning to include complete commercial landscape and facility maintenance services, too.

As stated, we offer a package of services that includes landscape, janitorial and facility services, which is largely unique in the industry.

We would like a design that communicates trust/partnership with a professional, corporate image, but not necessarily using the standard white business card. We would like a design that perhaps uses darker blues or perhaps a gray background, but we are open to other ideas. We might also be interested in a double-sided design - maybe with our logo on the back, printed on a gray background?

We will probably stick with the attached logo, but if you've got another inspired idea....

Target Market(s)

Property managers, commercial real estate professionals, corporate executives

Industry/Entity Type

Landscape

Requirements
Should not have
• Not interested in old style fonts.

```html
<!DOCTYPE html>
<html lang="en">
<head>
<meta charset="utf-8">
<title>Keystride Facility Services – Business Card</title>
<link rel="stylesheet" href="https://fonts.googleapis.com/css2?family=Questrial&display=swap">
<style>
  :root {
    --page-bg: #d9d6d1;
    --card-black: #020207;
    --card-navy: #2a2d4a;
    --card-deep: #0b0b1c;
    --silver: #c9c9cf;
    --silver-dim: #a9a9b1;
    --glow-blue: #0b0f3a;
  }
  * { box-sizing: border-box; margin: 0; padding: 0; }
  html, body {
    width: 1200px; height: 900px; overflow: hidden;
    background: var(--page-bg);
    font-family: "Questrial", "Century Gothic", sans-serif;
  }
  .canvas { position: relative; width: 1200px; height: 900px; }
  .card {
    position: absolute; left: 339px; width: 548px; height: 305px; overflow: hidden;
    box-shadow: 0 2px 6px rgba(0,0,0,.35);
  }
  .card--front {
    top: 113px;
    background: radial-gradient(ellipse 60% 65% at 50% 50%, var(--card-navy) 0%, var(--card-deep) 60%, var(--card-black) 100%);
  }
  .card--back {
    top: 444px;
    background: radial-gradient(ellipse 38% 60% at 45% 55%, var(--glow-blue) 0%, #05061a 50%, var(--card-black) 100%);
  }
  .frame { position: absolute; inset: 0; }
  .brand { position: absolute; display: flex; align-items: flex-start; color: var(--silver); }
  .brand__mark { border: 2px solid var(--silver); flex: none; }
  .brand__name { text-transform: uppercase; line-height: 1; }
  .card--front .brand { left: 18px; top: 17px; }
  .card--front .brand__mark { width: 46px; height: 46px; }
  .card--front .brand__text { margin-left: 7px; margin-top: 5px; }
  .card--front .brand__name--main { font-size: 20px; letter-spacing: 2.2px; }
  .card--front .brand__name--sub { font-size: 12.5px; letter-spacing: 1.6px; margin-top: 2px; }
  .tagline { font-size: 6.3px; margin-top: 4px; color: var(--silver); letter-spacing: .1px; }
  .card--back .brand { left: 78px; top: 113px; }
  .card--back .brand__mark { width: 39px; height: 37px; }
  .card--back .brand__text { margin-left: 5px; margin-top: 2px; }
  .card--back .brand__name--main { font-size: 17px; letter-spacing: 1.6px; }
  .card--back .brand__name--sub { font-size: 10px; letter-spacing: 1.4px; margin-top: 2px; }
  .divider { position: absolute; left: 273px; top: 61px; width: 1px; height: 161px; background: #3a3a48; }
  .contact { position: absolute; left: 284px; color: var(--silver); }
  .contact__label { top: 80px; font-size: 15px; letter-spacing: .6px; }
  .contact__name { top: 105px; font-size: 12px; color: var(--silver-dim); }
  .contact__role { top: 122px; font-size: 12px; color: var(--silver-dim); }
  .contact__web { top: 176px; font-size: 13px; letter-spacing: .2px; }
  .contact__phone { top: 194px; font-size: 13px; }
</style>
</head>
<body>
<main class="canvas">
  <section class="card card--front" aria-label="Card front">
    <svg class="frame" width="548" height="305" viewBox="0 0 548 305" aria-hidden="true">
      <defs>
        <linearGradient id="silverLine" x1="0" y1="0" x2="1" y2="1">
          <stop offset="0" stop-color="#e0e0e6"/>
          <stop offset=".5" stop-color="#8d8d96"/>
          <stop offset="1" stop-color="#d4d4da"/>
        </linearGradient>
      </defs>
      <polyline points="64,15.5 536.5,15.5 536.5,290.5 16.5,290.5 16.5,63" fill="none" stroke="url(#silverLine)" stroke-width="2.5"/>
    </svg>
    <div class="brand">
      <span class="brand__mark"></span>
      <div class="brand__text">
        <p class="brand__name brand__name--main">Keystride</p>
        <p class="brand__name brand__name--sub">Facility Services</p>
        <p class="tagline">One Source For Landscape, Janitorial and Facility Maintenance</p>
      </div>
    </div>
  </section>

  <section class="card card--back" aria-label="Card back">
    <div class="brand">
      <span class="brand__mark"></span>
      <div class="brand__text">
        <p class="brand__name brand__name--main">Keystride</p>
        <p class="brand__name brand__name--sub">Facility Services</p>
      </div>
    </div>
    <span class="divider"></span>
    <p class="contact contact__label">NAME SURNAME</p>
    <p class="contact contact__name">Marcus Hale</p>
    <p class="contact contact__role">General Manager</p>
    <p class="contact contact__web">www.keystridefacilityservices.com</p>
    <p class="contact contact__phone">000-000-0000</p>
  </section>
</main>
</body>
</html>
```